Organizational health infographic

I work as an independent contractor with a larger consulting firm named "the Lantern Works" https://www.lanternworks-example.com/ I need a simple infographic that visually explains the 3 stages of our client engagement, and their respective steps and objectives. Im inclined to use a "subway" map system design (Ive included a a draft overview of the content (in PPT and a PDF) and b) a few sample subway style infographics. I

Target Market(s)

CEOs and Human Resources Officers

Font styles to use
Sans Serif

Colors

Designer to choose colors to be used in the design.

Requirements
Must have
• my contact info
• martin kell 555-304-8821
• martin.kell@lanternworksadvisory-example.com
• lantern works logo (I put it near the top center part of the page). Logo and book pictures can be found on the website https://www.lanternworks-example.com
Nice to have
• 1) the more consistent the font and colors are with the Lantern Works website, the better https://www.lanternworks-example.com
• 2) if its possible to have all 3 "subway lines" collapse into a single timeline, that would be cool.
• 3) If its possible to add a visual timeline that shows each stage taking approx 3 to 6 months, also cool.
• 4) in stage 3, Im not sure about whether to use the actual book pictures or simply the titles of each book at a "subway stop" circle.

```html
<!DOCTYPE html>
<html lang="en">
<head>
<meta charset="utf-8">
<title>Lantern Works – Engagement Roadmap</title>
<link rel="stylesheet" href="https://fonts.googleapis.com/css2?family=Arimo:ital,wght@0,400;0,700;1,400;1,700&family=Montserrat:wght@400;500;700&display=swap">
<style>
  :root{
    --backdrop:#e4e4e6;
    --paper:#f2f2f3;
    --navy:#1e2236;
    --ink:#23242a;
    --muted:#4a4c55;
    --red:#c8202e;
    --blue:#2a9bd3;
    --green:#177a3a;
    --book-gray:#9a9a9a;
    --book-light:#d0d3dc;
    --book-gold:#c2a15a;
    --book-coral:#d54a3b;
  }
  *{box-sizing:border-box;margin:0;padding:0}
  html,body{width:1180px;height:1200px;overflow:hidden;background:var(--backdrop)}
  .sheet{position:absolute;left:206px;top:0;width:768px;height:1200px;background:var(--paper);font-family:"Arimo",Arial,sans-serif;color:var(--ink);overflow:hidden}
  .brand{position:absolute;left:34px;top:56px;display:flex;align-items:center;gap:12px}
  .brand-dot{width:46px;height:46px;border-radius:50%;background:var(--red)}
  .brand-name{font-family:"Montserrat",sans-serif;font-weight:500;font-size:50px;color:var(--navy);letter-spacing:-1px;line-height:1}
  .contact{position:absolute;right:40px;top:56px;text-align:right}
  .contact-name{font-family:"Montserrat",sans-serif;font-size:34px;color:var(--navy);line-height:1.1;margin-bottom:8px}
  .contact-name b{font-weight:700}
  .contact-name span{font-weight:400}
  .contact-line{font-style:italic;font-size:14.5px;line-height:16px;color:var(--navy)}
  .rule{position:absolute;left:36px;top:179px;width:692px;height:4px;background:var(--navy)}
  .diagram{position:absolute;left:0;top:0}
  .diagram text{font-family:"Arimo",Arial,sans-serif}
  .stage-title{font-weight:700;font-size:22px;letter-spacing:2px;fill:var(--ink)}
  .banner-text{font-size:16px;fill:#fff}
  .stop-label{font-size:10px;fill:var(--muted)}
  .stop-label-bold{font-size:11px;font-weight:700;fill:var(--ink)}
  .track-note{font-size:10.5px;font-style:italic;fill:var(--ink)}
  .objectives{position:absolute;left:499px;width:240px}
  .obj-stage1{top:246px}
  .obj-stage2{top:505px}
  .obj-stage3{top:797px}
  .obj-head{font-weight:700;font-size:14px;letter-spacing:3px;margin-bottom:8px}
  .obj-head.red{color:var(--red)} .obj-head.blue{color:var(--blue)} .obj-head.green{color:var(--green)}
  .obj-group{margin-bottom:9px}
  .obj-sub{font-style:italic;font-size:11px;color:var(--ink);margin-bottom:2px}
  .obj-sub.plain{font-style:normal;font-size:13px;margin-top:6px;margin-bottom:6px}
  .obj-list{list-style:none;padding-left:10px}
  .obj-list li{font-size:10px;line-height:12px;color:var(--muted);position:relative;padding-left:7px}
  .obj-list li::before{content:"";position:absolute;left:0;top:4px;width:3px;height:3px;border-radius:50%}
  .red-dots li::before{background:var(--red)} .blue-dots li::before{background:var(--blue)}
  .obj-text{font-size:10px;line-height:12px;color:var(--muted);padding-left:12px}
  .legend{position:absolute;left:0;top:1086px;width:768px;height:114px;background:var(--navy)}
  .legend text{font-family:"Arimo",Arial,sans-serif}
  .legend-label{font-size:8px;font-style:italic;fill:#fff}
  .book-label{font-size:8px;fill:#fff;letter-spacing:.3px}
</style>
</head>
<body>
<div class="sheet">
  <div class="brand">
    <div class="brand-dot"></div>
    <div class="brand-name">lantern works</div>
  </div>
  <div class="contact">
    <div class="contact-name"><b>martin</b> <span>kell</span></div>
    <div class="contact-line">555-304-8821</div>
    <div class="contact-line">martin.kell@lanternworksadvisory-example.com</div>
    <div class="contact-line">www.lanternworks-example.com</div>
  </div>
  <div class="rule"></div>

  <svg class="diagram" width="768" height="1086" viewBox="0 0 768 1086">
    <g fill="none" stroke="var(--navy)" stroke-width="3" stroke-dasharray="6 5">
      <path d="M140 254 H90 Q80 254 80 264 V358"/>
      <path d="M346 254 H410"/>
      <path d="M427 403 V484 Q427 494 417 494 H346"/>
      <path d="M140 505 H90 Q80 505 80 515 V614"/>
      <path d="M427 676 V776 Q427 786 417 786 H346"/>
      <path d="M140 800 H90 Q80 800 80 810 V925"/>
    </g>

    <!-- Stage 1 -->
    <text class="stage-title" x="242" y="247" text-anchor="middle">STAGE 1</text>
    <rect x="140" y="252" width="206" height="23" fill="var(--red)"/>
    <text class="banner-text" x="243" y="269" text-anchor="middle">Excutive Launch</text>
    <circle cx="422" cy="253" r="12" fill="var(--red)"/>
    <line x1="100" y1="381" x2="405" y2="381" stroke="var(--navy)" stroke-width="3"/>
    <circle cx="78" cy="381" r="22" fill="var(--paper)" stroke="var(--red)" stroke-width="4"/>
    <circle cx="185" cy="381" r="11" fill="var(--red)"/>
    <circle cx="248" cy="381" r="11" fill="var(--red)"/>
    <circle cx="329" cy="381" r="19" fill="var(--paper)" stroke="var(--red)" stroke-width="4"/>
    <polygon points="403,361 451,361 427,403" fill="var(--paper)" stroke="var(--red)" stroke-width="4"/>
    <text class="stop-label-bold" x="83" y="425" text-anchor="middle">2 Day</text>
    <text class="stop-label" x="185" y="416" text-anchor="middle">Meeting</text>
    <text class="stop-label" x="185" y="427" text-anchor="middle">Audits</text>
    <text class="stop-label" x="248" y="416" text-anchor="middle">Leader</text>
    <text class="stop-label" x="248" y="427" text-anchor="middle">Coaching</text>
    <text class="stop-label" x="329" y="416" text-anchor="middle">Quarterly</text>
    <text class="stop-label" x="329" y="427" text-anchor="middle">Off Sites</text>

    <!-- Stage 2 -->
    <text class="stage-title" x="242" y="489" text-anchor="middle">STAGE 2</text>
    <rect x="140" y="495" width="206" height="23" fill="var(--blue)"/>
    <text class="banner-text" x="243" y="512" text-anchor="middle">Next Level Rollout</text>
    <rect x="152" y="546" width="195" height="17" rx="8.5" fill="var(--navy)"/>
    <text x="249" y="558" text-anchor="middle" style="font-size:11px;fill:#fff">Key leader conferences</text>
    <g fill="none" stroke="var(--navy)" stroke-width="3">
      <path d="M96 625 L150 596"/>
      <path d="M180 588 H414 Q427 588 427 601 V628"/>
      <path d="M96 648 L150 680"/>
      <path d="M183 693 H318"/>
    </g>
    <circle cx="78" cy="636" r="22" fill="var(--paper)" stroke="var(--blue)" stroke-width="4"/>
    <circle cx="165" cy="588" r="15" fill="var(--paper)" stroke="var(--blue)" stroke-width="4"/>
    <circle cx="253" cy="588" r="15" fill="var(--paper)" stroke="var(--blue)" stroke-width="4"/>
    <circle cx="336" cy="588" r="15" fill="var(--paper)" stroke="var(--blue)" stroke-width="4"/>
    <circle cx="165" cy="693" r="18" fill="var(--paper)" stroke="var(--blue)" stroke-width="4"/>
    <circle cx="223" cy="693" r="9" fill="var(--blue)"/>
    <circle cx="281" cy="693" r="9" fill="var(--blue)"/>
    <circle cx="336" cy="693" r="18" fill="var(--paper)" stroke="var(--blue)" stroke-width="4"/>
    <polygon points="403,631 451,631 427,676" fill="var(--paper)" stroke="var(--blue)" stroke-width="4"/>
    <text class="stop-label-bold" x="80" y="677" text-anchor="middle">Key Leader</text>
    <text class="stop-label-bold" x="80" y="689" text-anchor="middle">Kicko</text>
    <text class="stop-label" x="223" y="664" text-anchor="middle">Meeting</text>
    <text class="stop-label" x="223" y="674" text-anchor="middle">Audits</text>
    <text class="stop-label" x="281" y="664" text-anchor="middle">Leader</text>
    <text class="stop-label" x="281" y="674" text-anchor="middle">Coaching</text>
    <text class="stop-label" x="165" y="728" text-anchor="middle">Department</text>
    <text class="stop-label" x="165" y="739" text-anchor="middle">Teams</text>
    <text class="stop-label" x="340" y="723" text-anchor="middle">Department</text>
    <text class="stop-label" x="340" y="734" text-anchor="middle">Rollouts</text>

    <!-- Stage 3 -->
    <text class="stage-title" x="242" y="784" text-anchor="middle">STAGE 3</text>
    <rect x="140" y="789" width="206" height="23" fill="var(--green)"/>
    <text class="banner-text" x="243" y="806" text-anchor="middle">Organizational Rollout</text>
    <g fill="none" stroke="var(--navy)" stroke-width="3">
      <path d="M94 932 L152 896"/>
      <path d="M178 890 H412 Q427 890 427 905 V925"/>
      <path d="M94 963 L152 1002"/>
      <path d="M178 1008 H412 Q427 1008 427 993 V970"/>
    </g>
    <circle cx="78" cy="947" r="22" fill="var(--paper)" stroke="var(--green)" stroke-width="4"/>
    <rect x="152" y="877" width="26" height="26" fill="var(--paper)" stroke="var(--green)" stroke-width="4"/>
    <rect x="152" y="995" width="26" height="26" fill="var(--paper)" stroke="var(--green)" stroke-width="4"/>
    <polygon points="403,925 451,925 427,968" fill="var(--paper)" stroke="var(--green)" stroke-width="4"/>
    <circle cx="224" cy="847" r="5" fill="var(--red)"/>
    <circle cx="275" cy="847" r="5" fill="var(--book-gray)"/>
    <circle cx="325" cy="847" r="5" fill="var(--book-light)"/>
    <circle cx="372" cy="847" r="5" fill="var(--book-gold)"/>
    <rect x="210" y="857" width="34" height="58" fill="var(--red)" role="img" aria-label="Cover of The Four Frictions of a Crew"/>
    <rect x="258" y="857" width="34" height="58" fill="#b9b9bb" role="img" aria-label="Cover of The Steady Crew Member"/>
    <rect x="308" y="857" width="34" height="58" fill="#dcdee4" role="img" aria-label="Cover of The Facts About Staff Commitment"/>
    <rect x="356" y="857" width="34" height="58" fill="var(--book-gold)" role="img" aria-label="Cover of Lost in Meetings"/>
    <circle cx="358" cy="962" r="5" fill="var(--book-coral)"/>
    <rect x="330" y="976" width="51" height="62" fill="var(--book-coral)" role="img" aria-label="Cover of Resolving the Four Frictions of a Crew"/>
    <text class="stop-label" x="165" y="915" text-anchor="middle">Workshops</text>
    <text class="stop-label" x="165" y="1037" text-anchor="middle">Internal</text>
    <text class="stop-label" x="165" y="1048" text-anchor="middle">Training</text>
    <text class="stop-label-bold" x="78" y="990" text-anchor="middle">Playbook</text>
    <text class="stop-label-bold" x="78" y="1002" text-anchor="middle">Rollout</text>
    <text class="track-note" x="210" y="999">Train the trainers</text>
    <text class="track-note" x="210" y="1019">Train the leaders</text>
  </svg>

  <div class="objectives obj-stage1">
    <div class="obj-head red">OBJECTIVES</div>
    <div class="obj-group"><div class="obj-sub">Team cohesion</div>
      <ul class="obj-list red-dots"><li>Solid trust</li><li>Aligned expectations</li></ul></div>
    <div class="obj-group"><div class="obj-sub">Playbook 1.0</div>
      <ul class="obj-list red-dots"><li>Aligned vision, values, strategy, priorities &amp; roles</li></ul></div>
    <div class="obj-group"><div class="obj-sub">Productive meetings</div>
      <div class="obj-sub">Consistent communication with greater org</div></div>
    <div class="obj-sub plain">Transition readiness</div>
    <ul class="obj-list red-dots"><li>Cohesion validation (CTAR)</li><li>Playbook Complete</li><li>Meeting Momentum</li></ul>
  </div>

  <div class="objectives obj-stage2">
    <div class="obj-head blue">OBJECTIVES</div>
    <div class="obj-group"><div class="obj-sub">Key leaders</div>
      <ul class="obj-list blue-dots"><li>Finish Playbook 2.0</li><li>Become Ambassadors Of Org Health</li><li>Cross Functional Cooperation &nbsp;Playbook 2.0</li></ul></div>
    <div class="obj-group"><div class="obj-sub">Department teams</div>
      <ul class="obj-list blue-dots"><li>Cohesion, Clarity, Productive Meetings</li></ul></div>
    <div class="obj-group"><div class="obj-sub">Department rollouts</div>
      <ul class="obj-list blue-dots"><li>Break Down Silos</li><li>Dept Priorities &nbsp;Align To Org Priorities</li></ul></div>
    <div class="obj-group"><div class="obj-sub">Transition readiness</div>
      <ul class="obj-list blue-dots"><li>Ctars Department</li><li>Core Values Detailed And Implemented</li></ul></div>
    <div class="obj-sub">Meeting Mastery</div>
  </div>

  <div class="objectives obj-stage3">
    <div class="obj-head green">OBJECTIVES</div>
    <div class="obj-group"><div class="obj-sub">All employees</div>
      <div class="obj-text">Understand and utilize the playbook<br>Are equipped &amp; motivated to create a healthy culture</div></div>
    <div class="obj-group" style="margin-top:14px"><div class="obj-sub">Transition readiness</div>
      <div class="obj-text">The consultation is completed when the leaders are ready to assume responsibility for maintaining a healthy culture.</div></div>
  </div>

  <svg class="legend" width="768" height="114" viewBox="0 0 768 114">
    <circle cx="48" cy="50" r="12" fill="none" stroke="#fff" stroke-width="3"/>
    <circle cx="109" cy="50" r="14" fill="#fff"/>
    <polygon points="157,39 183,39 170,62" fill="none" stroke="#fff" stroke-width="3"/>
    <rect x="220" y="39" width="22" height="22" fill="none" stroke="#fff" stroke-width="3"/>
    <text class="legend-label" x="48" y="83" text-anchor="middle">Live Off Site</text>
    <text class="legend-label" x="109" y="83" text-anchor="middle">Video</text>
    <text class="legend-label" x="109" y="93" text-anchor="middle">Conference</text>
    <text class="legend-label" x="170" y="83" text-anchor="middle">Transition</text>
    <text class="legend-label" x="170" y="93" text-anchor="middle">Evaluation</text>
    <text class="legend-label" x="231" y="83" text-anchor="middle">Training</text>
    <rect x="284" y="20" width="3" height="88" fill="var(--red)"/>
    <circle cx="343" cy="46" r="13" fill="var(--red)"/>
    <circle cx="430" cy="46" r="13" fill="var(--book-gray)"/>
    <circle cx="518" cy="46" r="13" fill="var(--book-light)"/>
    <circle cx="606" cy="46" r="13" fill="var(--book-gold)"/>
    <circle cx="694" cy="46" r="13" fill="var(--book-coral)"/>
    <g text-anchor="middle">
      <text class="book-label" x="343" y="74">THE FOUR</text><text class="book-label" x="343" y="84">FRICTIONS</text><text class="book-label" x="343" y="94">OF A CREW</text>
      <text class="book-label" x="430" y="74">THE STEADY</text><text class="book-label" x="430" y="84">CREW MEMBER</text>
      <text class="book-label" x="518" y="74">THE FACTS</text><text class="book-label" x="518" y="84">ABOUT STAFF</text><text class="book-label" x="518" y="94">COMMITMENT</text>
      <text class="book-label" x="606" y="74">LOST</text><text class="book-label" x="606" y="84">IN MEETINGS</text>
      <text class="book-label" x="694" y="74">RESOLVING THE</text><text class="book-label" x="694" y="84">FOUR FRICTIONS</text><text class="book-label" x="694" y="94">OF A CREW</text>
    </g>
  </svg>
</div>
</body>
</html>
```